I am in need of cover art for both an e-book and a paperback version for my latest book: The Ember Crown The Veiled Marches Volume 3

The novel is Swords and sorcery type fantasy with a strong half-elven lead. I am looking for an eye catching cover that goes somewhat with the first two--a fantastic cover that doesn't quite match is better than a mediocer one that does.
When you submit your cover art, it is imperitive that you state where you got the picture from.
The jacket blurb is as follows:
Separated by chance and fate, Toravin has to give up on finding love with Mira, instead he must watch helplessly as his kingdom is destroyed one city at a time. His enemies are vast in number and skillfully led, but they have no chance against the mighty fortress city of Calstwyn…or do they? Toravin begins to suspect he has been maneuvered into trapping himself exactly where his enemies want him.

Not wanting to be anywhere near Toravin when he weds another woman, Mira thinks she is leaving the world of magic and swords behind her, but by accident she comes across another fugitive from The Veiled Marches. However this fugitive is very much planning on returning and when he does he plans on bringing back something that can end the war in a flash.

Requirements
Must have
• Information on where cover art is obtained from

```html
<!DOCTYPE html>
<html lang="en">
<head>
<meta charset="utf-8">
<title>The Ember Crown – The Veiled Marches – Volume 3</title>
<link rel="stylesheet" href="https://fonts.googleapis.com/css2?family=Caveat+Brush&family=Kaushan+Script&display=swap">
<style>
  :root {
    --crimson-deep: #4a0303;
    --crimson: #9a0f0a;
    --scarlet: #d41c0e;
    --flame-orange: #f5621c;
    --flame-amber: #ffa42a;
    --flame-yellow: #ffe24c;
    --flame-white: #fffbe0;
    --title-cream: #ffe6b4;
    --title-edge: #b3140c;
    --subtitle-ink: #3a0604;
    --volume-white: #fffaf2;
    --grass-dark: #240302;
  }
  * { margin: 0; padding: 0; box-sizing: border-box; }
  html, body {
    width: 868px;
    height: 1200px;
    overflow: hidden;
    background: var(--crimson-deep);
  }
  .cover {
    position: relative;
    width: 868px;
    height: 1200px;
    overflow: hidden;
    background:
      radial-gradient(ellipse 120% 80% at 50% 30%, var(--scarlet) 0%, var(--crimson) 55%, var(--crimson-deep) 100%);
    font-family: "Caveat Brush", cursive;
  }
  .cover__flames {
    position: absolute;
    left: 0;
    top: 0;
    width: 868px;
    height: 640px;
    background:
      radial-gradient(ellipse 26% 22% at 47% 6%, var(--flame-white) 0%, var(--flame-yellow) 45%, rgba(255,226,76,0) 100%),
      radial-gradient(ellipse 12% 48% at 50% 30%, rgba(255,236,140,0.9) 0%, rgba(255,164,42,0.5) 50%, rgba(255,164,42,0) 100%),
      radial-gradient(ellipse 10% 40% at 36% 26%, rgba(255,200,70,0.8) 0%, rgba(245,98,28,0) 100%),
      radial-gradient(ellipse 10% 38% at 62% 24%, rgba(255,200,70,0.75) 0%, rgba(245,98,28,0) 100%),
      radial-gradient(ellipse 45% 60% at 48% 18%, var(--flame-amber) 0%, rgba(245,98,28,0.7) 40%, rgba(212,28,14,0) 100%),
      radial-gradient(ellipse 70% 75% at 50% 20%, rgba(245,98,28,0.55) 0%, rgba(212,28,14,0) 100%);
  }
  .cover__horizon {
    position: absolute;
    left: 0;
    bottom: 0;
    width: 868px;
    height: 330px;
    background:
      linear-gradient(to bottom, rgba(36,3,2,0) 0%, rgba(36,3,2,0) 55%, rgba(36,3,2,0.85) 72%, var(--grass-dark) 100%),
      radial-gradient(ellipse 55% 16% at 62% 42%, var(--flame-yellow) 0%, var(--flame-amber) 35%, rgba(245,98,28,0.5) 65%, rgba(154,15,10,0) 100%),
      radial-gradient(ellipse 40% 10% at 25% 55%, rgba(255,164,42,0.8) 0%, rgba(154,15,10,0) 100%);
  }
  .cover__title {
    position: absolute;
    left: 0;
    top: 430px;
    width: 868px;
    display: flex;
    justify-content: center;
    align-items: baseline;
    gap: 22px;
    font-weight: 400;
    line-height: 1;
    color: var(--title-cream);
    text-shadow: 0 0 4px var(--title-edge), 3px 3px 0 var(--title-edge);
    transform: rotate(-6deg);
  }
  .cover__title-small { font-size: 100px; }
  .cover__title-large {
    font-size: 150px;
    color: var(--flame-yellow);
    text-transform: uppercase;
  }
  .cover__title-medium { font-size: 112px; }
  .cover__subtitle {
    position: absolute;
    left: 40px;
    top: 620px;
    width: 868px;
    text-align: center;
    font-family: "Kaushan Script", cursive;
    font-weight: 400;
    font-size: 70px;
    color: var(--subtitle-ink);
    text-shadow: 0 0 8px rgba(255,120,60,0.35);
    transform: rotate(-6deg);
  }
  .cover__volume {
    position: absolute;
    left: 0;
    top: 860px;
    width: 868px;
    text-align: center;
    font-size: 64px;
    color: var(--volume-white);
    transform: rotate(-3deg);
  }
</style>
</head>
<body>
  <main class="cover">
    <div class="cover__flames" role="img" aria-label="Blazing sun bursting into long streaming tongues of flame that pour down from the top of the cover"></div>
    <div class="cover__horizon" role="img" aria-label="Glowing golden horizon of fire behind a silhouetted line of tall grass"></div>
    <h1 class="cover__title">
      <span class="cover__title-small">The</span>
      <span class="cover__title-large">Ember</span>
      <span class="cover__title-medium">Crown</span>
    </h1>
    <h2 class="cover__subtitle">The Veiled Marches</h2>
    <p class="cover__volume">Volume 3</p>
  </main>
</body>
</html>
```